Brochure Design Project for Building Designer

I need a modern and edgy brochure to introduce my new business LURO Design, Commercial and Residential Building Designers.

We specialise in Building Design, Project Management and Design Consultation.

I would like the brochure to be anywhere between 2-4 pages, depending of amount of suitable content available.
Colours to be black and white with splashes of
bright colours (mostly incorporated in photos).

Main Content of brochure to be broken up into 3 (maybe 4) sections to include:

About Us
Services
Projects

Logo Text (DESIGN etc) can be changed to white if suits better with black background.

Would be nice to include sketches to give it that architectural feel.

Samples and wording will be uploaded shortly
Updates

I HAVE PROVIDED A COMPLETE UPDATE OF PROJECT REQUIREMENTS INCLUDING ALL NEW UPLOADED FILES.

PLEASE REFER TO THE BROCHURE LAYOUT PDF UPLOADEDĀ FOR FULL INFORMATION ON PROJECT INCLUDING BROCHURE LAYOUT.

IF YOU HAVE ANY QUESTIONS OR REQUIRE ANY FURTHER INFORMATION, PLEASE LET ME KNOW

I HAVE ADDED FURTHER DEVELOPED PDF DOCUMENTS OF BROCHURE.

IF YOU HAVE TROUBLE OPENING THESE DOCS IN ADOBE ILLUSTRATOR THRU ADOBE BRIDGE PLEASE LET ME KNOW & I WILL UPLOAD AI FILES.

CAN YOU PLEASE FINE TUNE GRAPHICS AND WORK ON BACKGROUND

Target Market(s)

Builders, Property Developers, Architects, Consultants, Professionals

Industry/Entity Type

Business

Requirements
Must have
• Very Professional Look
Black and White
Simple and easy to read layout
Either A4 (if only 2 pages) or
A3 double sided with centre fold (if 4 pages)
Touch up of photos (if possible) to make them stand out of the page.
Samples of recent projects with photos
Should not have
• Any comics or similar

```html
<!DOCTYPE html>
<html lang="en">
<head>
<meta charset="utf-8">
<title>LURO Design – Brochure Concept 3</title>
<link rel="stylesheet" href="https://fonts.googleapis.com/css2?family=Josefin+Sans:wght@300;400&family=Maven+Pro:wght@400;700&family=Roboto+Condensed:wght@400&family=Cinzel:wght@400&display=swap">
<style>
  :root {
    --board: #ece7df;
    --strip: #ffffff;
    --tan: #b29f84;
    --tan-dark: #9c8b72;
    --slate: #575550;
    --slate-line: #4d4b47;
    --paper: #ffffff;
    --paper-shade: #dcdcdc;
    --lime: #a3c75c;
    --ink: #1e1e1e;
    --white: #ffffff;
  }
  * { margin: 0; padding: 0; box-sizing: border-box; }
  html, body { width: 1200px; height: 900px; overflow: hidden; }
  body { position: relative; background: var(--board); font-family: "Maven Pro", sans-serif; }

  .board { position: absolute; inset: 0 0 100px 0; background: var(--board); }

  .page {
    position: absolute; top: 93px; width: 513px; height: 562px;
    box-shadow: 0 2px 6px rgba(0,0,0,.25);
    overflow: hidden;
  }
  .page--cover { left: 56px; background: var(--slate); }
  .page--back  { left: 622px; background: var(--slate); }

  .band { position: absolute; left: 0; width: 100%; }
  .band--rule-light { background: var(--paper); }
  .band--rule-dark  { background: var(--slate-line); }
  .band--hero { top: 138px; height: 174px; background: linear-gradient(90deg, var(--paper-shade) 0%, var(--paper) 12%, var(--paper) 88%, var(--paper-shade) 100%); }
  .band--foot { top: 525px; height: 37px; background: linear-gradient(90deg, var(--paper-shade) 0%, var(--paper) 15%, var(--paper) 85%, #e6e6e6 100%); }

  .wordmark { position: absolute; white-space: nowrap; }
  .wordmark__name { font-family: "Maven Pro", sans-serif; font-weight: 700; color: var(--lime); letter-spacing: .02em; }
  .wordmark__tag { display: block; font-family: "Maven Pro", sans-serif; font-weight: 400; color: var(--ink); }

  .cover-mark { left: 59px; top: 184px; }
  .cover-mark .wordmark__name { font-size: 52px; line-height: 60px; }
  .cover-mark .wordmark__tag { font-size: 8.4px; margin-top: 4px; letter-spacing: .01em; }

  .photo { position: absolute; }
  .cover-photo { left: 320px; top: 175px; width: 145px; height: 118px;
    background: linear-gradient(160deg, #8a8a8a 0%, #5a5a5a 45%, #d8d8d8 100%); }

  .quote { position: absolute; left: 60px; top: 370px; font-family: "Josefin Sans", sans-serif; font-weight: 400;
    color: var(--white); font-size: 22px; line-height: 38px; letter-spacing: .09em; text-transform: uppercase; }
  .quote__author { position: absolute; left: 342px; top: 452px; font-family: "Cinzel", serif; font-size: 9px;
    letter-spacing: .12em; color: var(--white); }

  .back-photo--facade { left: 0; top: 0; width: 193px; height: 143px; background: linear-gradient(180deg, #7d7d7d 0%, #c9c9c9 55%, #6a6a6a 100%); }
  .back-photo--sketch { left: 200px; top: 0; width: 191px; height: 143px; background: linear-gradient(150deg, #f4f4f4 0%, #9a9a9a 55%, #e8e8e8 100%); }
  .back-photo--bedroom { left: 38px; top: 311px; width: 220px; height: 178px; background: linear-gradient(135deg, #d0d0d0 0%, #8a8a8a 50%, #3c3c3c 100%); }
  .back-photo--living { left: 270px; top: 311px; width: 185px; height: 251px; background: linear-gradient(180deg, #e6e6e6 0%, #b5b5b5 45%, #2e2e2e 100%); }

  .intro { position: absolute; left: 36px; top: 163px; width: 450px; font-family: "Roboto Condensed", sans-serif;
    font-size: 21.5px; line-height: 33.5px; color: var(--lime); text-transform: uppercase; letter-spacing: .005em; }

  .back-mark { left: 35px; top: 500px; }
  .back-mark .wordmark__name { font-size: 24px; line-height: 28px; }
  .back-mark .wordmark__tag { font-size: 4px; color: var(--white); margin-top: 1px; }

  .label { position: absolute; font-family: "Maven Pro", sans-serif; font-size: 17px; color: var(--tan-dark); }
  .label--cover { left: 56px; top: 711px; }
  .label--back { left: 622px; top: 715px; }

  .caption-strip { position: absolute; left: 0; top: 800px; width: 1200px; height: 100px; background: var(--strip); }
  .caption { position: absolute; left: 35px; top: 36px; font-family: "Maven Pro", sans-serif; font-size: 26px;
    color: var(--tan); letter-spacing: .06em; white-space: nowrap; }
  .caption strong { font-weight: 700; }
  .caption .caption__note { letter-spacing: .03em; }
</style>
</head>
<body>
  <div class="board">
    <section class="page page--cover" aria-label="Brochure cover">
      <div class="band band--rule-light" style="top:125px;height:9px"></div>
      <div class="band band--rule-dark" style="top:134px;height:4px"></div>
      <div class="band band--hero"></div>
      <div class="band band--rule-dark" style="top:312px;height:5px"></div>
      <div class="band band--rule-light" style="top:317px;height:8px"></div>
      <div class="band band--foot"></div>

      <div class="wordmark cover-mark">
        <span class="wordmark__name">LURO <span style="color:var(--ink);font-size:20px;letter-spacing:.18em">DESIGN</span></span>
        <span class="wordmark__tag">COMMERCIAL &amp; RESIDENTIAL BUILDING DESIGNERS</span>
      </div>
      <div class="photo cover-photo" role="img" aria-label="Two-storey modern house rendering fading into an architectural wireframe sketch"></div>

      <p class="quote">Simplicity is<br>the ultimate<br>sophistication</p>
      <p class="quote__author">Marco Delvani</p>
    </section>

    <section class="page page--back" aria-label="Brochure back page">
      <div class="photo back-photo--facade" role="img" aria-label="Black and white photo of a modern commercial building facade"></div>
      <div class="photo back-photo--sketch" role="img" aria-label="Modern house rendering blended with a line sketch"></div>

      <p class="intro">We offer high quality drafting solutions for pre-designed projects of anysize to ensure you get the best quality drawings for local authority +construction issue.</p>

      <div class="photo back-photo--bedroom" role="img" aria-label="Black and white photo of a modern bedroom interior"></div>
      <div class="photo back-photo--living" role="img" aria-label="Black and white photo of an open living and dining space with a staircase"></div>

      <div class="wordmark back-mark">
        <span class="wordmark__name">LURO <span style="color:var(--white);font-size:9px;letter-spacing:.18em">DESIGN</span></span>
        <span class="wordmark__tag">COMMERCIAL &amp; RESIDENTIAL BUILDING DESIGNERS</span>
      </div>
    </section>

    <p class="label label--cover">cover</p>
    <p class="label label--back">back</p>
  </div>

  <div class="caption-strip">
    <p class="caption">BROCHURE DESIGN - <strong>CONCEPT 3.</strong> <span class="caption__note">(4 page version)</span></p>
  </div>
</body>
</html>
```